Plakat-Design für LD & Kapitän Funkel
Zielgruppe
Musikformation
Folkrockgeigerin trifft Liedermacher
Eisenkrugpublikum Schnittmenge Valentin Heuberg
Aufgabenstellung
Unteres Drittel darf nicht mit Text bedruckt sein, da dort der Veranstalter Datum und Location draufklebt
zu verarbeitender Text:
Lena Dorothea & Kapitän Funkel
Folkrockgeigerin (bekannt von Eisenkrug (Eisenkrug bitte in bremen bold)) trifft Liedermacher
brandneues Programm: Gläserne Wolken
Es sollen A3 und A4 Poster hochkant werden, leider gibt´s nur querformat Fotos...

```html
<!DOCTYPE html>
<html lang="de">
<head>
<meta charset="utf-8">
<title>Lena Dorothea + Kapitän Funkel – Gläserne Wolken</title>
<link rel="stylesheet" href="https://fonts.googleapis.com/css2?family=Oswald:wght@400;700&family=Metamorphous&display=swap">
<style>
  :root {
    --page: #ffffff;
    --gold: #b39452;
    --gold-light: #e2cd8e;
    --ink-white: #ffffff;
    --ink-silver: #d9d6d2;
    --stone-light: #b9ab97;
    --stone: #8f8170;
    --stone-dark: #5e5244;
    --wood: #7d4d2f;
    --coat-red: #b3281f;
    --rug-red: #5a1f1c;
    --shade: #1d1713;
    --sticker-area: #ffffff;
  }
  * { box-sizing: border-box; margin: 0; padding: 0; }
  html, body {
    width: 887px; height: 1200px; overflow: hidden;
    background: var(--page);
  }
  .poster {
    position: absolute;
    left: 64px; top: 56px;
    width: 762px; height: 1081px;
    background: var(--sticker-area);
    overflow: hidden;
  }
  .gold-rule {
    position: absolute; left: 0; width: 100%; height: 6px;
    background: linear-gradient(90deg, var(--gold), var(--gold-light) 50%, var(--gold));
  }
  .gold-rule--top { top: 0; }
  .gold-rule--bottom { bottom: 0; }
  .duo-photo {
    position: absolute; left: 0; top: 6px;
    width: 100%; height: 856px;
    background:
      linear-gradient(180deg, rgba(29,23,19,0) 50%, rgba(29,23,19,.35) 72%, rgba(29,23,19,.7) 100%),
      linear-gradient(90deg, var(--wood) 0%, #8a5a38 18%, var(--stone) 30%, var(--stone-light) 50%, var(--stone) 62%, #a23a2c 72%, #9b3a2c 86%, var(--stone-dark) 100%),
      var(--stone);
  }
  .duo-photo::after {
    content: ""; position: absolute; left: 0; right: 0; bottom: 0; height: 38%;
    background: linear-gradient(90deg, var(--shade) 0%, #3a3a45 25%, var(--rug-red) 55%, #3b3030 80%, var(--rug-red) 100%);
    opacity: .75;
  }
  .headline {
    position: absolute; left: 0; width: 100%;
    text-align: center; color: var(--ink-white);
    font-family: "Oswald", sans-serif;
    line-height: 1.3;
    text-shadow: 0 1px 3px rgba(0,0,0,.5);
  }
  .tagline {
    top: 34px; font-size: 17px; font-weight: 400; letter-spacing: .03em;
  }
  .tagline .band-name { font-weight: 700; font-size: 22px; letter-spacing: .02em; }
  .stars {
    position: absolute; left: 0; width: 100%;
    text-align: center; color: var(--ink-white);
    font-size: 22px; letter-spacing: 4px; line-height: 1;
    text-shadow: 0 1px 3px rgba(0,0,0,.5);
  }
  .stars--top { top: 68px; }
  .stars--mid { top: 632px; }
  .stars--bottom { top: 828px; }
  .program-label {
    top: 512px; font-size: 23px; font-weight: 400; letter-spacing: .03em;
  }
  .program-title {
    top: 548px; font-size: 56px; font-weight: 400;
    color: var(--ink-silver); letter-spacing: .02em; line-height: 1.3;
  }
  .artist {
    position: absolute; left: 0; width: 100%;
    text-align: center; white-space: nowrap;
    font-family: "Metamorphous", serif;
    font-weight: 400; line-height: 1.2;
    text-shadow: 0 2px 6px rgba(0,0,0,.6);
  }
  .artist--lead { top: 654px; font-size: 70px; color: var(--ink-white); }
  .artist--guest { top: 736px; font-size: 60px; color: var(--ink-silver); }
</style>
</head>
<body>
  <main class="poster">
    <div class="gold-rule gold-rule--top"></div>
    <div class="duo-photo" role="img" aria-label="Foto: Geigerin mit Drehleier und Liedermacher in roter Jacke mit Mandoline, vor Steinmauer auf einem Teppich sitzend, umgeben von Geigen und Gitarren"></div>

    <p class="headline tagline">FOLKROCKGEIGERIN (BEKANNT VON <span class="band-name">EISENKRUG</span>) TRIFFT LIEDERMACHER</p>
    <div class="stars stars--top">★★★</div>

    <p class="headline program-label">BRANDNEUES PROGRAMM:</p>
    <h2 class="headline program-title">GLÄSERNE WOLKEN</h2>
    <div class="stars stars--mid">★★★</div>

    <h1 class="artist artist--lead">LENA DOROTHEA</h1>
    <p class="artist artist--guest">+ KAPITÄN FUNKEL</p>
    <div class="stars stars--bottom">★★★</div>

    <div class="gold-rule gold-rule--bottom"></div>
  </main>
</body>
</html>
```